Australian Dairy Business Requires Packaging Concept

We are an Australian Dairy Products Supplier exporting our goods predominantly to China including Baby Formula/Long Life Milk and Full Cream Milk Powder. We are looking for only conceptual art at this stage so we can synchronise with the most suitable designer.

The range incorporates the following and we have nicknamed the brand "Pomsa" while in concept

1. "Pomsa" Infant Formula Pack

Artwork is common but 3 colours in range are needed to denote 0-6months /6 -12 Months /1 Year olds + ( I have attached a crude mock up to assist in the explanantion and dont worry too much about the text its more the style of the design
We need key factors such as an illustrative Kangaroo and an illustrative Map of Australia - The size of each illustration does not matter let your creative skills dictate the best proportions. The Mock up brand name can be called "Pomsa".

2. "Pomsa" 1KG Full Cream Milk Powder

The artwork here is for 1 variety only with the look and style to be very similar to the Infant Formula however instead of a Kangaroo we would like an illustrative cow light brown in colour and again a illustrative map of Australia.I have attached a picture of the size of the box and the text is not in important at this stage just the concept within the range.

3. Pomsa" 1 Litre Long Life MilkJerry

The artwork here is for 1 variety only with the look and style to be almost identical to the Full Cream Milk Powder.I have attached a picture of a typical sized long lide box box and the text is not important at this stage just the concept within the range.

Target Market(s)

Infant Formual Packs - Asian Parents who trust imported
goods from Australia

Milk Powder - Broad Chinese Demographic but consumer
based towards 25-60 yr old women

Milk Long Life - Broad Chiense Demographic consumer based with more equal spread of men and women 25-60yr old

Industry/Entity Type

Business

Requirements
Must have
• Infant Formual Packs can be fun in design but still professional so that marketing campaign can reinforce in future as a trusted brand and product.
Nice to have
• Range of products need to look like a family although subtle difference are welcom. At this stage we just want to seek out a concept.

```html
<!DOCTYPE html>
<html lang="en">
<head>
<meta charset="utf-8">
<title>Pomsa Dairy Packaging Range</title>
<link rel="stylesheet" href="https://fonts.googleapis.com/css2?family=Kalam:wght@400;700&family=Nunito:wght@400;600&display=swap">
<style>
  :root {
    --stage: #6a6a6a;
    --white: #ffffff;
    --green: #22ad86;
    --green-tint: #d9f5ec;
    --green-deep: #8fdcc3;
    --purple: #a4589f;
    --purple-tint: #f6ddf3;
    --purple-deep: #e3a9dd;
    --red: #d8365c;
    --red-tint: #fcd6de;
    --red-deep: #f5a3b5;
    --blue: #1aa3d6;
    --blue-tint: #cfeefa;
    --blue-deep: #8fd5f0;
    --kangaroo-tan: #d8a060;
    --cow-brown: #a8643a;
  }
  * { box-sizing: border-box; margin: 0; padding: 0; }
  html, body { width: 1200px; height: 667px; overflow: hidden; }
  body { background: var(--stage); position: relative; }

  .pack {
    position: absolute;
    top: 98px;
    width: 205px;
    height: 444px;
    overflow: hidden;
    background:
      repeating-linear-gradient(90deg, rgba(255,255,255,0.5) 0 3px, transparent 3px 11px),
      linear-gradient(180deg, var(--tint) 0%, var(--tint-deep) 100%);
  }
  .pack--newborn { left: 30px;  --accent: var(--green);  --tint: var(--green-tint);  --tint-deep: var(--green-deep);  --mascot: var(--kangaroo-tan); }
  .pack--infant  { left: 254px; --accent: var(--purple); --tint: var(--purple-tint); --tint-deep: var(--purple-deep); --mascot: var(--kangaroo-tan); }
  .pack--toddler { left: 479px; --accent: var(--red);    --tint: var(--red-tint);    --tint-deep: var(--red-deep);    --mascot: var(--kangaroo-tan); }
  .pack--powder  { left: 740px; --accent: var(--blue);   --tint: var(--blue-tint);   --tint-deep: var(--blue-deep);   --mascot: var(--cow-brown); }
  .pack--longlife{ left: 964px; --accent: var(--blue);   --tint: var(--blue-tint);   --tint-deep: var(--blue-deep);   --mascot: var(--kangaroo-tan); }

  .pack__brand {
    position: absolute;
    top: 12px; left: 0; right: 0;
    text-align: center;
    font-family: "Kalam", cursive;
    font-weight: 700;
    font-size: 58px;
    line-height: 1;
    color: var(--accent);
  }
  .pack__product {
    position: absolute;
    top: 88px; left: 14px;
    font-family: "Kalam", cursive;
    font-weight: 700;
    color: var(--accent);
    line-height: 1;
    transform: rotate(-4deg);
    transform-origin: left top;
    z-index: 2;
  }
  .pack__product-main { display: block; font-size: 20px; }
  .pack__product-sub  { display: block; font-size: 16px; padding-left: 8px; }

  .pack__art {
    position: absolute;
    top: 112px; left: 8px;
    width: 190px; height: 230px;
    background:
      radial-gradient(ellipse 32% 30% at 48% 38%, var(--mascot) 0%, var(--mascot) 45%, transparent 100%),
      radial-gradient(ellipse 52% 40% at 52% 60%, var(--accent) 0%, var(--accent) 55%, transparent 100%);
    opacity: 0.9;
  }

  .pack__base {
    position: absolute;
    left: 0; bottom: 0;
    width: 205px; height: 130px;
  }
  .pack__label {
    position: absolute;
    bottom: 24px; left: 0; right: 0;
    display: flex; align-items: center; justify-content: center; gap: 8px;
    font-family: "Nunito", sans-serif;
    font-size: 14px;
    color: var(--accent);
  }
  .icon-dot { width: 20px; height: 20px; border-radius: 50%; background: var(--accent); }
  .icon-size {
    width: 26px; height: 24px; border-radius: 4px;
    background: var(--accent); color: var(--white);
    font-family: "Nunito", sans-serif; font-weight: 600; font-size: 10px;
    display: flex; align-items: center; justify-content: center;
  }
</style>
</head>
<body>

  <section class="pack pack--newborn">
    <div class="pack__brand">Pomsa</div>
    <div class="pack__art" role="img" aria-label="Illustrated kangaroo holding a bottle, seated on a map of Australia"></div>
    <div class="pack__product"><span class="pack__product-main">Infant</span><span class="pack__product-sub">Formula Pack</span></div>
    <svg class="pack__base" viewBox="0 0 205 130" aria-hidden="true"><path d="M0 20 Q100 58 205 30 L205 130 L0 130 Z" fill="#fff"/><path d="M0 20 Q100 58 205 30" fill="none" stroke="var(--accent)" stroke-width="2" opacity=".5"/></svg>
    <div class="pack__label"><span class="icon-dot"></span>0-6 Months</div>
  </section>

  <section class="pack pack--infant">
    <div class="pack__brand">Pomsa</div>
    <div class="pack__art" role="img" aria-label="Illustrated kangaroo holding a bottle, seated on a map of Australia"></div>
    <div class="pack__product"><span class="pack__product-main">Infant</span><span class="pack__product-sub">Formula Pack</span></div>
    <svg class="pack__base" viewBox="0 0 205 130" aria-hidden="true"><path d="M0 20 Q100 58 205 30 L205 130 L0 130 Z" fill="#fff"/><path d="M0 20 Q100 58 205 30" fill="none" stroke="var(--accent)" stroke-width="2" opacity=".5"/></svg>
    <div class="pack__label"><span class="icon-dot"></span>6 -12 Months</div>
  </section>

  <section class="pack pack--toddler">
    <div class="pack__brand">Pomsa</div>
    <div class="pack__art" role="img" aria-label="Illustrated kangaroo holding a bottle, seated on a map of Australia"></div>
    <div class="pack__product"><span class="pack__product-main">Infant</span><span class="pack__product-sub">Formula Pack</span></div>
    <svg class="pack__base" viewBox="0 0 205 130" aria-hidden="true"><path d="M0 20 Q100 58 205 30 L205 130 L0 130 Z" fill="#fff"/><path d="M0 20 Q100 58 205 30" fill="none" stroke="var(--accent)" stroke-width="2" opacity=".5"/></svg>
    <div class="pack__label"><span class="icon-dot"></span>1 Year olds +</div>
  </section>

  <section class="pack pack--powder">
    <div class="pack__brand">Pomsa</div>
    <div class="pack__art" role="img" aria-label="Illustrated light brown cow waving, standing on a map of Australia"></div>
    <div class="pack__product"><span class="pack__product-main">Full Cream</span><span class="pack__product-sub">Milk Powder</span></div>
    <svg class="pack__base" viewBox="0 0 205 130" aria-hidden="true"><path d="M0 42 Q50 38 80 20 Q100 6 120 22 Q160 44 205 40 L205 130 L0 130 Z" fill="#fff"/></svg>
    <div class="pack__label"><span class="icon-size">1kg</span></div>
  </section>

  <section class="pack pack--longlife">
    <div class="pack__brand">Pomsa</div>
    <div class="pack__art" role="img" aria-label="Illustrated kangaroo holding a bottle, seated on a map of Australia"></div>
    <div class="pack__product"><span class="pack__product-main">Long Life</span><span class="pack__product-sub">Milk</span></div>
    <svg class="pack__base" viewBox="0 0 205 130" aria-hidden="true"><path d="M0 34 Q20 10 40 30 Q60 50 80 20 Q100 0 120 26 Q140 48 160 18 Q180 2 205 30 L205 130 L0 130 Z" fill="#fff"/></svg>
    <div class="pack__label"><span class="icon-size">1L</span></div>
  </section>

</body>
</html>
```